Business Card Design

I need a card design for Melbourne based business in Australia, called M P Concrete Services. We Concrete and excavate. Concreteing is main part of business.Commercial ,Residential and industrial.We want to be known as M P C (services) as form of abbreviation.We would like to highlight the initials with contact phone. A clean straight edge design. We have no color preference and would prefer a design that can easily be used on all parts of our business including clothing,vechiles and stationary

Industry/Entity Type

Business

Contact Information for Business Card

Hugh 0491 570 156
Peter 0491 570 157
mpcsercices@quollmail.com

```html
<!DOCTYPE html>
<html lang="en">
<head>
<meta charset="utf-8">
<title>M P Concrete – Business Card</title>
<link href="https://fonts.googleapis.com/css2?family=Source+Sans+3:wght@300;400&display=swap" rel="stylesheet">
<style>
  :root {
    --page-bg: #ffffff;
    --card-bg: #4a494b;
    --card-edge: #bdbdbd;
    --title-ink: #ffffff;
    --body-ink: #ececec;
  }
  html, body {
    margin: 0;
    padding: 0;
    width: 1200px;
    height: 740px;
    overflow: hidden;
    background: var(--page-bg);
  }
  .canvas {
    position: relative;
    width: 1200px;
    height: 740px;
    font-family: "Source Sans 3", "Source Sans Pro", Arial, sans-serif;
    font-weight: 300;
  }
  .card {
    position: absolute;
    left: 43px;
    top: 43px;
    width: 1114px;
    height: 654px;
    background: var(--card-bg);
    box-shadow: 0 0 4px 1px var(--card-edge);
  }
  .card > * {
    position: absolute;
    margin: 0;
    line-height: 1;
    white-space: nowrap;
  }
  .brand-name {
    left: 33px;
    top: 128px;
    font-size: 150px;
    font-weight: 300;
    color: var(--title-ink);
    letter-spacing: -1px;
  }
  .tagline {
    left: 33px;
    top: 272px;
    font-size: 30px;
    color: var(--body-ink);
  }
  .contact-list {
    left: 33px;
    top: 556px;
    font-size: 31px;
    color: var(--body-ink);
    list-style: none;
    padding: 0;
  }
  .contact-list li {
    display: flex;
    height: 42px;
  }
  .contact-name {
    width: 162px;
  }
  .email {
    right: 35px;
    top: 575px;
    font-size: 33px;
    color: var(--body-ink);
  }
</style>
</head>
<body>
  <main class="canvas">
    <section class="card">
      <h1 class="brand-name">M P Concrete</h1>
      <p class="tagline">Commercial ,Residential and industrial concreting</p>
      <ul class="contact-list">
        <li><span class="contact-name">Hugh</span><span class="contact-phone">0491 570 156</span></li>
        <li><span class="contact-name">Peter</span><span class="contact-phone">0491 570 157</span></li>
      </ul>
      <p class="email">mpcsercices@quollmail.com</p>
    </section>
  </main>
</body>
</html>
```